Business Card Design

We need a business card design for a Non-Profit Christian Based Organization located in Milford, Pa.
Alder Ridge Helping Harbor
Is a Christ-centered organization dedicated to providing compassion and hope to homeless or near homeless, families and individuals, by meeting their basic and urgent need of food, clothing and shelter.
Updates
the logo is black and white
and must add the color green some where 00400
Industry/Entity Type
Clothing
Contact Information for Business Card
Alder Ridge Helping Harbor
P.O. Box 287
Fernbrook, Pa 18492
Phone: (570) 413-CARE(2273)
Toll Free: (855) 413-CARE
email:Info@alderridgehh.org
email:Careline@alderridgehh.org
Our organization already has a logo.
Front of card:
Is a Christ-centered organization dedicated to providing compassion and hope to homeless or near homes, families and individual by meeting their basic and urgent need of food, clothing and shelter.(this is our Mission Statement)
On back of card:
'I was hungry and you gave me something to eat;
"I was thirsty and you gave me something to drink;
"I was a stranger and you invited me in."
Matthew 25:35
Color: Logo is black and white
Background color I would like a bright light green 00ff00(close to that)
I attached a sample of what I created on Quill Press but, I don't like the color green, nor the design (but I just wanted to give you and Idea of the Logo and Alder Ridge (one line) Helping Harbor (second line) in a different font thank you
Delia Rostova
Pr/Board of Directors

```html
<!DOCTYPE html>
<html lang="en">
<head>
<meta charset="utf-8">
<title>Alder Ridge Helping Harbor – Business Card</title>
<link rel="stylesheet" href="https://fonts.googleapis.com/css2?family=Crimson+Text:wght@400;600;700&display=swap">
<style>
  :root {
    --backdrop: #2b2b2b;
    --leaf: #9cc43a;
    --leaf-light: #b2d548;
    --leaf-deep: #8db52c;
    --paper: #ffffff;
    --paper-shade: #e9e9e9;
    --ink: #111111;
  }
  html, body {
    margin: 0;
    width: 1200px;
    height: 900px;
    overflow: hidden;
    background: var(--backdrop);
    font-family: "Crimson Text", Georgia, serif;
    color: var(--ink);
  }
  .canvas {
    position: relative;
    width: 1200px;
    height: 900px;
  }
  .card {
    position: absolute;
    left: 320px;
    width: 560px;
    height: 320px;
    overflow: hidden;
    box-shadow: 0 10px 30px rgba(0,0,0,.5);
  }
  /* Back side */
  .card-back {
    top: 80px;
    background: linear-gradient(135deg, var(--leaf-light) 0%, var(--leaf) 55%, var(--leaf-deep) 100%);
  }
  .scripture {
    position: absolute;
    left: 34px;
    top: 70px;
    margin: 0;
    font-size: 21px;
    line-height: 1.35;
    font-weight: 600;
  }
  .scripture-ref {
    position: absolute;
    right: 30px;
    bottom: 40px;
    font-size: 19px;
    font-weight: 600;
  }
  /* Front side */
  .card-front {
    top: 480px;
    background: radial-gradient(ellipse at 55% 55%, var(--paper) 40%, var(--paper-shade) 100%);
  }
  .front-shapes {
    position: absolute;
    inset: 0;
  }
  .contact {
    position: absolute;
    margin: 0;
    font-size: 14px;
    line-height: 18px;
  }
  .contact-left { left: 22px; top: 14px; }
  .contact-left .org-line {
    display: block;
    margin-top: 2px;
    font-size: 18.5px;
    line-height: 24px;
  }
  .contact-right { left: 332px; top: 2px; }
  .tagline {
    position: absolute;
    left: 0;
    right: 0;
    top: 144px;
    margin: 0;
    text-align: center;
    font-size: 32px;
    line-height: 40px;
    font-weight: 700;
  }
  .org-mark {
    position: absolute;
    left: 0;
    right: 0;
    top: 190px;
    display: flex;
    justify-content: center;
    align-items: center;
    gap: 8px;
    font-size: 15px;
    line-height: 18px;
    font-weight: 600;
  }
  .org-mark-dot {
    width: 12px;
    height: 12px;
    border-radius: 50%;
    background: var(--ink);
  }
</style>
</head>
<body>
<main class="canvas">

  <section class="card card-back" aria-label="Back of card">
    <p class="scripture">"I was hungry and you gave me something to<br>eat; "I was thirsty and you gave me something to<br>drink; "I was a stranger and you invited me in."</p>
    <span class="scripture-ref">Matthew 25:35</span>
  </section>

  <section class="card card-front" aria-label="Front of card">
    <svg class="front-shapes" viewBox="0 0 560 320" width="560" height="320" aria-hidden="true">
      <rect x="180" y="0" width="120" height="13" fill="var(--leaf)"/>
      <rect x="332" y="40" width="228" height="10" fill="var(--leaf)"/>
      <rect x="300" y="84" width="260" height="18" fill="var(--leaf)"/>
      <path d="M560 118 C 530 210, 330 240, 0 252" fill="none" stroke="var(--leaf)" stroke-width="4"/>
      <path d="M0 264 C 250 264, 470 232, 560 155 L 560 205 C 470 260, 250 285, 0 282 Z" fill="var(--leaf)"/>
      <rect x="0" y="300" width="560" height="20" fill="var(--leaf)"/>
    </svg>

    <p class="contact contact-left">
      Phone: (570) 413-CARE(2273)<br>
      Email:Careline@alderridgehh.org
      <span class="org-line">Alder Ridge Helping Harbor P.O. Box 287 Fernbrook, Pa 18492</span>
    </p>
    <p class="contact contact-right">
      Toll Free: (855) 413-CARE<br>
      Email:Info@alderridgehh.org
    </p>

    <h1 class="tagline">Christ-Centered Organization</h1>
    <div class="org-mark">
      <span class="org-mark-dot"></span>
      <span>Alder Ridge Helping Harbor</span>
    </div>
  </section>

</main>
</body>
</html>
```